Wedding Poster Based on Classic Movie Posters

We would like to create a poster for our wedding that is based on a classic movie poster. Attached are a couple example movie posters and pictures of Marlene and me.

The poster should include the following:
1. "Marlene Trowbridge" and "Gerald Pemberly" as the lead actors.
2. Movie title: Beneath the Lanterns: An Evening Tale
3. 1st review quote: "Holy Matrimony" -Ledgerline
4. 2nd review quote: "A Match Made in Heaven" -The Bellwether

Target Market(s)

A wedding party to use as a decoration .

Requirements
Must have
• 1. "Marlene Trowbridge" and "Gerald Pemberly" as the lead actors, 2. Movie title: Beneath the Lanterns: An Evening Tale, 3. 1st review quote: "Holy Matrimony" -Ledgerline, 4. 2nd review quote: "A Match Made in Heaven" -The Bellwether
Nice to have
• The background could be Washington, DC, Miami, New York City, Paris, London, Amsterdam, or Berlin.

```html
<!DOCTYPE html>
<html lang="en">
<head>
<meta charset="utf-8">
<title>Beneath the Lanterns: An Evening Tale</title>
<link href="https://fonts.googleapis.com/css2?family=Chewy&family=Poppins:ital,wght@0,600;0,700;1,600&display=block" rel="stylesheet">
<style>
  :root {
    --orange: #ff8200;
    --stage: #c98a47;
    --ink: #050404;
    --paper: #f4f2f0;
    --card: #8a5238;
    --photo-night: #2b2a3a;
    --photo-dark: #3a2a20;
    --photo-mid: #6b4a30;
    --photo-warm: #c7954a;
    --photo-glow: #f2c66a;
    --fleck: #fbf3e6;
  }
  html, body { margin: 0; padding: 0; overflow: hidden; background: #ffffff; }
  .poster {
    position: relative;
    width: 848px;
    height: 1200px;
    overflow: hidden;
    background: var(--orange);
    font-family: "Poppins", sans-serif;
  }
  .poster__art { position: absolute; inset: 0; width: 848px; height: 1200px; }

  .title {
    position: absolute;
    left: 0;
    width: 848px;
    margin: 0;
    text-align: center;
    font-family: "Chewy", "Sniglet", system-ui, sans-serif;
    font-weight: 400;
    color: var(--paper);
    -webkit-text-stroke: 18px var(--ink);
    paint-order: stroke fill;
    white-space: nowrap;
    line-height: 1;
  }
  .title__word { display: inline-block; }
  .title--main { top: 432px; font-size: 80px; letter-spacing: 1px; }
  .title--main .title__word--a { transform: translateY(22px) rotate(-7deg); }
  .title--main .title__word--b { transform: translateY(-2px) rotate(-1deg); }
  .title--main .title__word--c { transform: translateY(14px) rotate(8deg); }
  .title--sub { top: 548px; font-size: 86px; }

  .credits {
    position: absolute;
    left: 116px;
    top: 680px;
    width: 616px;
    height: 260px;
    color: var(--paper);
    text-align: center;
  }
  .credits p { margin: 0; }
  .credits__name { font-weight: 700; font-size: 39px; line-height: 46px; }
  .credits__name--first { margin-top: 32px !important; }
  .credits__amp { font-weight: 700; font-size: 34px; line-height: 44px; }
  .credits__role { font-weight: 600; font-style: italic; font-size: 28px; line-height: 34px; margin-top: 10px !important; }

  .review {
    position: absolute;
    top: 993px;
    width: 313px;
    height: 170px;
    margin: 0;
    background: var(--card);
    color: var(--paper);
    text-align: center;
    font-weight: 600;
    display: flex;
    flex-direction: column;
    justify-content: center;
    box-sizing: border-box;
    padding: 0 10px;
  }
  .review--left { left: 96px; }
  .review--right { left: 433px; }
  .review__quote { margin: 0; font-size: 27px; line-height: 30px; }
  .review__source { margin: 14px 0 0; font-size: 24px; line-height: 1; }
</style>
</head>
<body>
<main class="poster">
  <svg class="poster__art" viewBox="0 0 848 1200" xmlns="http://www.w3.org/2000/svg">
    <defs>
      <linearGradient id="photoTone" x1="0" y1="0" x2="1" y2="1">
        <stop offset="0" stop-color="var(--photo-night)"/>
        <stop offset="0.35" stop-color="var(--photo-dark)"/>
        <stop offset="0.7" stop-color="var(--photo-mid)"/>
        <stop offset="1" stop-color="var(--photo-dark)"/>
      </linearGradient>
      <radialGradient id="glowLeft" cx="0.2" cy="0.38" r="0.3">
        <stop offset="0" stop-color="var(--photo-warm)" stop-opacity="0.75"/>
        <stop offset="1" stop-color="var(--photo-warm)" stop-opacity="0"/>
      </radialGradient>
      <radialGradient id="glowRight" cx="0.8" cy="0.42" r="0.32">
        <stop offset="0" stop-color="var(--photo-warm)" stop-opacity="0.7"/>
        <stop offset="1" stop-color="var(--photo-warm)" stop-opacity="0"/>
      </radialGradient>
      <radialGradient id="glowCenter" cx="0.4" cy="0.55" r="0.18">
        <stop offset="0" stop-color="var(--photo-glow)" stop-opacity="0.55"/>
        <stop offset="1" stop-color="var(--photo-glow)" stop-opacity="0"/>
      </radialGradient>
      <clipPath id="photoShape">
        <path d="M0 0 H848 V636 C760 672 560 702 424 702 C260 702 110 662 0 590 Z"/>
      </clipPath>
    </defs>

    <path class="stage-floor" d="M0 982 L424 893 L848 978 L848 1200 L0 1200 Z" fill="var(--stage)"/>

    <g class="hero-photo" role="img" aria-label="Photo of the couple smiling at a lantern-lit café table in the evening" clip-path="url(#photoShape)">
      <rect width="848" height="710" fill="url(#photoTone)"/>
      <rect width="848" height="710" fill="url(#glowLeft)"/>
      <rect width="848" height="710" fill="url(#glowRight)"/>
      <rect width="848" height="710" fill="url(#glowCenter)"/>
    </g>

    <path class="credits-plate" d="M118 684 L150 677 L300 683 L500 677 L732 683 L729 800 L734 935 L600 941 L400 935 L200 942 L121 938 L116 820 Z" fill="var(--ink)"/>

    <g class="speckle" fill="var(--fleck)" opacity="0.85">
      <ellipse cx="62" cy="48" rx="2" ry="4"/><ellipse cx="190" cy="120" rx="1.5" ry="3"/>
      <ellipse cx="320" cy="70" rx="2" ry="5" transform="rotate(20 320 70)"/><ellipse cx="455" cy="160" rx="1.5" ry="3"/>
      <ellipse cx="560" cy="40" rx="2" ry="4"/><ellipse cx="690" cy="100" rx="3" ry="8" transform="rotate(-25 690 100)"/>
      <ellipse cx="790" cy="210" rx="1.5" ry="3"/><ellipse cx="120" cy="260" rx="2" ry="4"/>
      <ellipse cx="270" cy="330" rx="1.5" ry="3"/><ellipse cx="400" cy="240" rx="2" ry="5" transform="rotate(15 400 240)"/>
      <ellipse cx="600" cy="300" rx="2" ry="4"/><ellipse cx="735" cy="350" rx="1.5" ry="3"/>
      <ellipse cx="40" cy="400" rx="2" ry="4"/><ellipse cx="340" cy="420" rx="1.5" ry="3"/>
      <ellipse cx="520" cy="390" rx="2" ry="5"/><ellipse cx="805" cy="430" rx="2" ry="4"/>
      <ellipse cx="20" cy="640" rx="2" ry="5"/><ellipse cx="60" cy="760" rx="1.5" ry="4"/>
      <ellipse cx="90" cy="870" rx="2" ry="5" transform="rotate(-15 90 870)"/><ellipse cx="30" cy="940" rx="1.5" ry="3"/>
      <ellipse cx="780" cy="700" rx="2" ry="5"/><ellipse cx="820" cy="800" rx="3" ry="5" transform="rotate(40 820 800)"/>
      <ellipse cx="760" cy="900" rx="1.5" ry="4"/><ellipse cx="830" cy="930" rx="2" ry="4"/>
      <ellipse cx="95" cy="930" rx="3" ry="8" transform="rotate(20 95 930)"/><ellipse cx="280" cy="975" rx="5" ry="3"/>
      <ellipse cx="520" cy="975" rx="2" ry="4"/><ellipse cx="430" cy="1000" rx="3" ry="8" transform="rotate(15 430 1000)"/>
      <ellipse cx="50" cy="1050" rx="1.5" ry="4"/><ellipse cx="810" cy="1060" rx="2" ry="5"/>
      <ellipse cx="760" cy="990" rx="1.5" ry="3"/><ellipse cx="620" cy="1180" rx="1.5" ry="4"/>
      <ellipse cx="240" cy="1185" rx="2" ry="3"/><ellipse cx="70" cy="1140" rx="2" ry="4"/>
    </g>
  </svg>

  <h1 class="title title--main"><span class="title__word title__word--a">Beneath</span> <span class="title__word title__word--b">the</span> <span class="title__word title__word--c">Lanterns</span></h1>
  <p class="title title--sub">An Evening Tale</p>

  <section class="credits">
    <p class="credits__name credits__name--first">“Marlene Trowbridge"</p>
    <p class="credits__amp">&amp;</p>
    <p class="credits__name">"Gerald Pemberly"</p>
    <p class="credits__role">as the lead actors</p>
  </section>

  <blockquote class="review review--left">
    <p class="review__quote">"Holy Matrimony"</p>
    <p class="review__source">-Ledgerline</p>
  </blockquote>
  <blockquote class="review review--right">
    <p class="review__quote">"A Match Made<br>in Heaven"</p>
    <p class="review__source">-The Bellwether</p>
  </blockquote>
</main>
</body>
</html>
```